Banner Ad to promote Youth Cycling Camps

We need a 728 x 90 banner ad to promote some youth cycling camps. There are 2 different camps - a road camp where they learn to ride their bikes on the roads and a mountain bike camp. The camps teach bike handling skills and racing tactics.

Target Market(s)

Parents of youth ages 7-17

Industry/Entity Type

Non-Profit

Font styles to use
Sans Serif

Requirements
Must have
• Logo
• Dates - Road Camp May 5-7, 2017
• - Mountain Bike Camp July 14-16, 2017
• website - quadrapedalcup.org
• be 728 x 90
Nice to have
• Animated - would like it to rotate with 3 slides - 1 a focus on both camps, 1 on road camp, 1 on mountain bike camp

```html
<!DOCTYPE html>
<html lang="en">
<head>
<meta charset="utf-8">
<title>Youth Cycling Camps – Banner Set</title>
<link rel="stylesheet" href="https://fonts.googleapis.com/css2?family=Bungee&family=Oswald:wght@500;600&family=Roboto+Condensed:wght@400;700&display=swap">
<style>
  :root {
    --ink: #0d0d0d;
    --paper: #ffffff;
    --sun: #f4e11c;
    --sky: #7fd9ee;
    --ring: #3ec7e6;
    --muted: #d8d8d8;
  }
  * { margin: 0; padding: 0; box-sizing: border-box; }
  html, body { width: 1200px; height: 638px; overflow: hidden; background: var(--paper); }
  .stage {
    position: relative; width: 770px; height: 410px;
    transform: scale(1.5584, 1.5561); transform-origin: 0 0;
  }
  .banner {
    position: absolute; left: 27px; width: 728px; height: 90px;
    background: var(--ink); overflow: hidden;
    font-family: "Oswald", "Arial Narrow", sans-serif; color: var(--paper);
  }
  .banner--both { top: 25px; }
  .banner--road { top: 162px; }
  .banner--mtb { top: 300px; }

  .photo { position: absolute; left: 0; top: 0; width: 728px; height: 72px;
    clip-path: polygon(467px 0, 728px 0, 728px 72px, 432px 72px); }
  .photo--road { background: linear-gradient(100deg, #4b5a3a 0%, #8a8f86 35%, #b8bcb4 55%, #6f7d55 75%, #9aa47a 100%); }
  .photo--mtb { background: linear-gradient(100deg, #8f3a5a 0%, #5f7a3a 30%, #3d4a2a 55%, #7c8f55 80%, #a8a070 100%); }

  .shapes { position: absolute; inset: 0; }

  .brand { position: absolute; left: 6px; top: 14px; width: 62px; height: 62px; border-radius: 50%;
    background: var(--ring); border: 5px solid var(--ink); outline: 2px solid var(--ring);
    display: flex; align-items: center; justify-content: center; text-align: center; }
  .brand__name { font-family: "Oswald", sans-serif; font-weight: 600; font-size: 7px; line-height: 1.1; color: var(--ink); letter-spacing: 0; }

  .headline { position: absolute; left: 82px; top: 2px; font-family: "Bungee", sans-serif;
    font-size: 16px; letter-spacing: .3px; color: var(--paper); white-space: nowrap; }

  .camp { position: absolute; left: 82px; font-weight: 600; white-space: nowrap; line-height: 1; }
  .camp--yellow { color: var(--sun); }
  .camp--white { color: var(--paper); }

  .coaches-note { position: absolute; left: 82px; top: 66px; font-family: "Roboto Condensed", sans-serif; font-size: 6.5px; line-height: 1.2; color: var(--paper); }
  .coaches-note b { font-size: 7px; }

  .ages { position: absolute; color: var(--ink); font-weight: 600; white-space: nowrap; line-height: 1; }
  .site { position: absolute; color: var(--ink); font-family: "Roboto Condensed", sans-serif; font-weight: 700; letter-spacing: 1.2px; white-space: nowrap; line-height: 1; }

  .tagline { position: absolute; left: 456px; top: 76px; font-family: "Roboto Condensed", sans-serif; font-size: 8.5px; color: var(--muted); white-space: nowrap; }
  .tagline b { color: var(--paper); font-weight: 700; }
</style>
</head>
<body>
<div class="stage">

  <!-- Slide 1: both camps -->
  <section class="banner banner--both">
    <div class="photo photo--road" role="img" aria-label="Photo of a group of young cyclists riding together"></div>
    <svg class="shapes" viewBox="0 0 728 90" width="728" height="90" aria-hidden="true">
      <polygon points="463,0 469,0 434,72 428,72" fill="var(--sun)"/>
      <polygon points="378,22 452,22 444,40 370,40" fill="var(--sky)"/>
      <polygon points="298,71 442,71 434,89 290,89" fill="var(--sun)"/>
    </svg>
    <div class="brand"><span class="brand__name">QUADRAPEDAL<br>CUP</span></div>
    <div class="headline">BEST CYCLING CAMPS FOR YOUTH</div>
    <div class="camp camp--yellow" style="top:25px;font-size:16px">ROAD CAMP <span class="camp--white">- MAY 5-7, 2017</span></div>
    <div class="camp camp--yellow" style="top:45px;font-size:16px">MOUNTAIN BIKE CAMP <span class="camp--white">- JULY 14-16, 2017</span></div>
    <div class="coaches-note"><b>PROFESSIONAL COACHES</b><br>Great Youth To Adult Ratio, Affordable</div>
    <div class="ages" style="left:388px;top:23px;font-size:14px">Ages 7-17</div>
    <div class="site" style="left:313px;top:74px;font-size:12px">quadrapedalcup.org</div>
    <div class="tagline"><b>PROFESSIONAL COACHES</b> Great Youth To Adult Ratio, Affordable</div>
  </section>

  <!-- Slide 2: road camp -->
  <section class="banner banner--road">
    <div class="photo photo--road" role="img" aria-label="Photo of young road cyclists riding in a group on a paved road"></div>
    <svg class="shapes" viewBox="0 0 728 90" width="728" height="90" aria-hidden="true">
      <polygon points="463,0 469,0 434,72 428,72" fill="var(--sun)"/>
      <polygon points="318,28 452,28 438,58 304,58" fill="var(--sky)"/>
      <polygon points="280,69 436,69 428,89 272,89" fill="var(--sun)"/>
    </svg>
    <div class="brand"><span class="brand__name">QUADRAPEDAL<br>CUP</span></div>
    <div class="headline">BEST CYCLING CAMPS FOR YOUTH</div>
    <div class="camp camp--yellow" style="top:23px;font-size:29px">ROAD CAMP</div>
    <div class="camp camp--white" style="top:58px;font-size:21px">MAY 5-7, 2017</div>
    <div class="ages" style="left:330px;top:32px;font-size:21px">Ages 7-17</div>
    <div class="site" style="left:294px;top:73px;font-size:13px">quadrapedalcup.org</div>
    <div class="tagline"><b>PROFESSIONAL COACHES</b> Great Youth To Adult Ratio, Affordable</div>
  </section>

  <!-- Slide 3: mountain bike camp -->
  <section class="banner banner--mtb">
    <div class="photo photo--mtb" role="img" aria-label="Photo of young mountain bikers riding a forest trail"></div>
    <svg class="shapes" viewBox="0 0 728 90" width="728" height="90" aria-hidden="true">
      <polygon points="484,0 490,0 455,72 449,72" fill="var(--sun)"/>
      <polygon points="330,26 452,26 438,56 316,56" fill="var(--sky)"/>
      <polygon points="280,69 436,69 428,89 272,89" fill="var(--sun)"/>
    </svg>
    <div class="brand"><span class="brand__name">QUADRAPEDAL<br>CUP</span></div>
    <div class="headline">BEST CYCLING CAMPS FOR YOUTH</div>
    <div class="camp camp--yellow" style="top:28px;font-size:20px">MOUNTAIN BIKE CAMP</div>
    <div class="camp camp--white" style="top:63px;font-size:18px">JULY 14-16, 2017</div>
    <div class="ages" style="left:338px;top:30px;font-size:21px">Ages 7-17</div>
    <div class="site" style="left:294px;top:73px;font-size:13px">quadrapedalcup.org</div>
    <div class="tagline"><b>PROFESSIONAL COACHES</b> Great Youth To Adult Ratio, Affordable</div>
  </section>

</div>
</body>
</html>
```